RT Staging & Design - a company built on first impressions, needs an impressive letterhead

Please create a letter head to be used for our project proposals, contract agreements and other client correspondence. We are a home Staging and interior design company. We like sleek, modern, clean and elegant design. Please create a document that compliments and uses our logo. We will also be creating flyers that we would like to match our letterhead and future marketing materials

Target Market(s)

real estate agents, home owners looking to sell

Industry/Entity Type

Interior Design

```html
<!DOCTYPE html>
<html lang="en">
<head>
<meta charset="utf-8">
<title>RT Staging &amp; Design — Letterhead</title>
<link href="https://fonts.googleapis.com/css2?family=Arimo:wght@400&display=swap" rel="stylesheet">
<style>
  :root {
    --backdrop: #d9d9d9;
    --paper: #ffffff;
    --ink: #6e6e6e;
    --charcoal: #3b3b3b;
    --steel: #8791a3;
    --steel-light: #b7bdc8;
    --watermark: #f0f0f0;
  }
  * { box-sizing: border-box; margin: 0; padding: 0; }
  html, body { width: 1200px; height: 784px; overflow: hidden; background: var(--backdrop); }
  .letterhead {
    position: absolute; left: 338px; top: 22px;
    width: 524px; height: 740px;
    background: var(--paper);
    box-shadow: 0 2px 10px rgba(0,0,0,.12);
    overflow: hidden;
  }
  .corner-bar { position: absolute; }
  .corner-bar--top-dark   { left: 0; top: 0; width: 46px; height: 5px; background: var(--charcoal); }
  .corner-bar--top-steel  { left: 46px; top: 0; width: 24px; height: 5px; background: var(--steel); }
  .corner-bar--right-dark { right: 0; top: 110px; width: 5px; height: 40px; background: var(--charcoal); }
  .corner-bar--right-steel{ right: 0; top: 150px; width: 5px; height: 22px; background: var(--steel); }
  .brand {
    position: absolute; right: 40px; top: 58px;
    display: flex; align-items: center; gap: 8px;
  }
  .brand__mark { width: 10px; height: 10px; border-radius: 50%; background: var(--charcoal); }
  .brand__name {
    font-family: "Arimo", sans-serif; font-weight: 400;
    font-size: 16px; color: var(--charcoal);
  }
  .letter-body {
    position: absolute; left: 58px; right: 40px; top: 120px;
    font-family: "Arimo", sans-serif; font-size: 8.6px; line-height: 1.32;
    color: var(--ink); text-align: justify;
  }
  .letter-body p { text-indent: 40px; margin-bottom: 11px; }
  .signature {
    position: absolute; left: 48px; top: 520px;
    width: 150px; height: 40px; background: var(--watermark); border-radius: 3px;
  }
  .watermark-name {
    position: absolute; left: 60px; top: 582px;
    font-family: "Arimo", sans-serif; font-weight: 400;
    font-size: 28px; color: var(--watermark);
  }
  .contact-bar {
    position: absolute; left: 16px; right: 16px; bottom: 18px;
    display: flex; gap: 12px; align-items: center;
    font-family: "Arimo", sans-serif; font-size: 7.6px; color: var(--ink);
    white-space: nowrap;
  }
  .contact-bar__item { display: flex; align-items: center; gap: 3px; }
  .contact-bar__item svg { width: 8px; height: 8px; fill: var(--ink); }
  .edge-band { position: absolute; bottom: 0; height: 8px; }
  .edge-band--dark  { left: 0; width: 250px; background: var(--charcoal); }
  .edge-band--steel { left: 262px; right: 0; background: linear-gradient(90deg, var(--steel), var(--steel-light)); }
  .edge-rule { position: absolute; left: 0; right: 0; bottom: 11px; height: 1px; background: var(--steel-light); }
  .side-bar { position: absolute; left: 0; bottom: 8px; width: 5px; height: 60px; background: var(--charcoal); }
</style>
</head>
<body>
<main class="letterhead">
  <span class="corner-bar corner-bar--top-dark"></span>
  <span class="corner-bar corner-bar--top-steel"></span>
  <span class="corner-bar corner-bar--right-dark"></span>
  <span class="corner-bar corner-bar--right-steel"></span>

  <header class="brand">
    <span class="brand__mark"></span>
    <span class="brand__name">RT Staging &amp; Design</span>
  </header>

  <section class="letter-body">
    <p>Lorem Ipsum is simply dummy text of the printing and typesetting industry. Lorem Ipsum has been the industry's standard dummy text ever since the 1500s, when an unknown printer took a galley of type and scrambled it to make a type specimen book. It has survived not only five centuries, but also the leap into electronic typesetting, remaining essentially unchanged. It was popularised in the 1960s with the release of Typeline sheets containing Lorem Ipsum passages, and more recently with desktop publishing software like PageForm Studio including versions of Lorem Ipsum.</p>
    <p>It is a long established fact that a reader will be distracted by the readable content of a page when looking at its layout. The point of using Lorem Ipsum is that it has a more-or-less normal distribution of letters, as opposed to using 'Content here, content here', making it look like readable English. Many desktop publishing packages and web page editors now use Lorem Ipsum as their default model text, and a search for 'lorem ipsum' will uncover many web sites still in their infancy. Various versions have evolved over the years, sometimes by accident, sometimes on purpose (injected humour and the like).</p>
    <p>Contrary to popular belief, Lorem Ipsum is not simply random text. It has roots in a piece of classical Latin literature from 45 BC, making it over 2000 years old. Edwin Carrow, a Latin professor at Marlow Hill College in Ashford, looked up one of the more obscure Latin words, consectetur, from a Lorem Ipsum passage, and going through the cites of the word in classical literature, discovered the undoubtable source. Lorem Ipsum comes from sections 1.10.32 and 1.10.33 of "de Finibus Bonorum et Malorum" structures, to generate Lorem Ipsum which looks reasonable. The generated Lorem Ipsum is therefore always free from repetition, injected humour, or non-characteristic words etc.</p>
  </section>

  <div class="signature" role="img" aria-label="Handwritten sign-off signature"></div>
  <div class="watermark-name" aria-hidden="true">RT Staging &amp; Design</div>

  <footer class="contact-bar">
    <span class="contact-bar__item"><svg viewBox="0 0 10 10"><path d="M5 0a3.5 3.5 0 0 0-3.5 3.5C1.5 6 5 10 5 10s3.5-4 3.5-6.5A3.5 3.5 0 0 0 5 0zm0 5a1.5 1.5 0 1 1 0-3 1.5 1.5 0 0 1 0 3z"/></svg>000 Example Street, Example US 0000</span>
    <span class="contact-bar__item"><svg viewBox="0 0 10 10"><rect x="1" y="3" width="8" height="6" rx="1"/><rect x="3" y="1" width="4" height="2"/></svg>0000 004 000</span>
    <span class="contact-bar__item"><svg viewBox="0 0 10 10"><path d="M2 1l2 0 1 2.5-1.2 1a6 6 0 0 0 2.7 2.7l1-1.2L10 7v2c0 .5-.5 1-1 1A9 9 0 0 1 0 1c0-.5.5-1 1-1z"/></svg>0000 000 000</span>
    <span class="contact-bar__item"><svg viewBox="0 0 10 10"><path d="M0 2h10v6H0zM0 2l5 3.5L10 2" stroke="#fff" stroke-width=".8"/></svg>Info@example.com</span>
    <span class="contact-bar__item"><svg viewBox="0 0 10 10"><circle cx="5" cy="5" r="4.5"/></svg>www.example.com</span>
  </footer>
  <span class="edge-rule"></span>
  <span class="side-bar"></span>
  <span class="edge-band edge-band--dark"></span>
  <span class="edge-band edge-band--steel"></span>
</main>
</body>
</html>
```